Branvique needs a business Card Design

We are looking for a business card Design for our new Managed Service Provider Company, Branvique. Branvique encompasses everything IT for the average medium sized business. Our primary services are help desk support, cyber-security (malware and ransomware protection), and Disaster Recovery systems. We would like the design to have a very clean and professional look, with a very minimalist feel.

Target Market(s)

Medium to large sized businesses

Industry/Entity Type

It Service

Contact Information for Business Card

Name GoesHere
name@branvique.com
O: 555-382-6047
C: 555-731-5820

Font styles to use
Other font styles liked:
• Poppins Font Only Please

Colors

Designer to choose only greyscale colors for use in the design.

Requirements
Must have
• Logo included
Nice to have
• Cutting Edge, innovative, minimalistic, elegant

```html
<!DOCTYPE html>
<html lang="en">
<head>
<meta charset="utf-8">
<title>Branvique Business Card</title>
<link href="https://fonts.googleapis.com/css2?family=Lato:wght@400;700;900&display=swap" rel="stylesheet">
<style>
  :root {
    --navy: #0c2340;
    --ink: #1c2230;
    --paper: #ffffff;
    --backdrop: #e4e5e8;
    --rule: #c9ccd2;
    --muted: #3a3f4a;
  }
  * { box-sizing: border-box; margin: 0; padding: 0; }
  html, body {
    width: 1200px; height: 900px; overflow: hidden;
    background: var(--backdrop);
    font-family: "Lato", sans-serif;
  }
  .sheet {
    width: 1200px; height: 900px;
    display: flex; flex-direction: column; align-items: center; justify-content: center;
    gap: 60px;
  }
  .card {
    width: 630px; height: 360px;
    position: relative;
    box-shadow: 0 8px 24px rgba(0,0,0,0.12);
  }
  /* Back */
  .card--back { background: var(--navy); color: var(--paper); }
  .card--back .wordmark {
    position: absolute; right: 70px; top: 100px;
    font-size: 28px; font-weight: 400; letter-spacing: 0.5em;
    color: var(--paper);
  }
  .services {
    position: absolute; right: 52px; bottom: 44px;
    text-align: right;
  }
  .services__title {
    font-size: 24px; font-weight: 900; margin-bottom: 8px; margin-right: 22px;
  }
  .services__list { list-style: none; }
  .services__list li {
    font-size: 17px; line-height: 1.45;
  }
  .services__list li::after {
    content: ""; display: inline-block; width: 6px; height: 6px; border-radius: 50%;
    background: var(--paper); margin-left: 12px; vertical-align: middle;
  }
  /* Front */
  .card--front { background: var(--paper); color: var(--ink); display: flex; align-items: center; }
  .brand {
    width: 310px; display: flex; align-items: center; justify-content: center; gap: 12px;
  }
  .brand__square { width: 14px; height: 14px; background: var(--navy); }
  .brand .wordmark {
    font-size: 24px; font-weight: 400; letter-spacing: 0.42em; color: var(--navy);
  }
  .divider { width: 1px; height: 200px; background: var(--rule); }
  .contact { padding-left: 36px; }
  .contact__name { font-size: 30px; font-weight: 900; color: var(--navy); line-height: 1.1; }
  .contact__role { font-size: 17px; color: var(--muted); margin-bottom: 20px; }
  .contact__list { list-style: none; }
  .contact__list li {
    display: flex; align-items: center; gap: 12px;
    font-size: 18px; line-height: 1.5; color: var(--ink);
  }
  .contact__list svg { width: 18px; height: 18px; flex: none; }
</style>
</head>
<body>
<main class="sheet">
  <section class="card card--back">
    <div class="wordmark">BRANVIQUE</div>
    <div class="services">
      <h2 class="services__title">SERVICES</h2>
      <ul class="services__list">
        <li>Help desk support</li>
        <li>Cyber-security</li>
        <li>Disaster Recovery systems</li>
      </ul>
    </div>
  </section>

  <section class="card card--front">
    <div class="brand">
      <span class="brand__square"></span>
      <span class="wordmark">BRANVIQUE</span>
    </div>
    <div class="divider"></div>
    <div class="contact">
      <h1 class="contact__name">GoesHere</h1>
      <p class="contact__role">Founder &amp; CEO</p>
      <ul class="contact__list">
        <li>
          <svg viewBox="0 0 20 20" aria-hidden="true"><path fill="#0c2340" d="M3 7c0-2 3-3 7-3s7 1 7 3v1h-4V7H7v1H3z M5 9h10l1 7H4z"/><circle cx="10" cy="12.5" r="2" fill="#fff"/></svg>
          555-382-6047
        </li>
        <li>
          <svg viewBox="0 0 20 20" aria-hidden="true"><rect x="5" y="1.5" width="10" height="17" rx="2" fill="none" stroke="#0c2340" stroke-width="2"/><rect x="8.5" y="15" width="3" height="1.5" fill="#0c2340"/></svg>
          555-731-5820
        </li>
        <li>
          <svg viewBox="0 0 20 20" aria-hidden="true"><rect x="1.5" y="4" width="17" height="12" fill="#0c2340"/><path d="M2 4.5l8 6 8-6M2 15.5l6-5M18 15.5l-6-5" stroke="#fff" stroke-width="1.2" fill="none"/></svg>
          name@branvique.com
        </li>
        <li>
          <svg viewBox="0 0 20 20" aria-hidden="true"><circle cx="10" cy="10" r="8" fill="none" stroke="#0c2340" stroke-width="1.8"/><path d="M2 10h16M10 2c-3 3-3 13 0 16M10 2c3 3 3 13 0 16M4 6h12M4 14h12" stroke="#0c2340" stroke-width="1.2" fill="none"/></svg>
          www.branvique.com
        </li>
      </ul>
    </div>
  </section>
</main>
</body>
</html>
```